New singe page website for our software development company

We need a single webpage that includes information about our company, contact details and a job posting. It should scroll vertically with some cool animations and parallax scrolling effects.

We are a software development consulting company that writes custom software for our customers. The webpage should have graphics and illustrations that illustrate this.

Find our logo attached, it can be modified as needed.

Thanks for all the design. When looking through the various design it's clear to us, that car related images does not look right.

We got to have software design/engineering images instead.

Our unique selling points are:

• Custom software development
• Project Managment
• Industry Services
We want these displayed with some text and icons. The icons should either have the red/brown colour from our logo, or a colour that matches the design

Software

```html
<!DOCTYPE html>
<html lang="en">
<head>
<meta charset="utf-8">
<title>Keelstone – Custom Software Development</title>
<link href="https://fonts.googleapis.com/css2?family=Lato:ital,wght@0,300;0,400;0,700;1,400&display=swap" rel="stylesheet">
<style>
:root{
  --brand:#8a2a12;
  --brand-dark:#6e1f0c;
  --text:#333;
  --muted:#555;
  --rule:#c9c9c9;
  --band:#ededed;
  --band-dark:#d2d2d2;
  --footer:#2f2f2f;
  --hero-a:#3d4f6f;
  --hero-b:#a9b7d6;
}
*{box-sizing:border-box;margin:0;padding:0}
html,body{width:682px;height:1200px;overflow:hidden}
body{font-family:'Lato',sans-serif;color:var(--text);background:#fff;position:relative}
.abs{position:absolute}
.brand-name{font-weight:700;color:var(--brand);font-size:15px;display:flex;align-items:center;gap:5px;white-space:nowrap}
.brand-name i{width:7px;height:7px;background:var(--brand);display:block}

/* header */
.site-header{top:0;left:0;width:682px;height:62px;background:#fff}
.phone{top:10px;left:480px;font-size:10.5px;display:flex;align-items:center;gap:5px;white-space:nowrap}
.main-nav{top:44px;left:373px;display:flex;font-size:8px}
.main-nav a{color:var(--text);text-decoration:none;padding:0 6px;border-left:1px solid #777;line-height:10px}
.main-nav a:first-child{border:0;color:var(--brand);border-bottom:2px solid var(--brand);padding-bottom:3px}

/* hero */
.hero{top:62px;left:0;width:682px;height:264px;background:linear-gradient(90deg,var(--hero-a),#6d80a8 45%,var(--hero-b))}
.hero-art{top:0;left:0;width:400px;height:264px;background:radial-gradient(circle at 45% 45%,#c8d6ea,#5a6b8d 55%,#2d3649)}
.hero-copy{top:55px;left:413px;color:#fff}
.hero-copy .kicker{color:var(--brand);font-size:20px;line-height:22px;font-weight:300}
.hero-copy h1{font-weight:300;color:#222;font-size:21px;line-height:23px;margin-top:2px}
.hero-copy .sub{color:#222;font-size:13px;line-height:13px;letter-spacing:.5px;font-weight:300}
.hero-copy p{font-size:7.2px;line-height:11px;margin-top:12px;width:190px}
.hero-copy .btn{display:inline-block;margin-top:10px;background:#f2f2f2;color:#222;font-size:9px;font-weight:700;padding:6px 8px;border-radius:2px}
.slide-arrow{width:24px;height:24px;border-radius:50%;background:rgba(80,90,110,.6);border:1px solid rgba(255,255,255,.6)}

/* services */
.services-band{top:326px;left:0;width:682px;height:60px;background:var(--band)}
.services{top:302px;left:74px;width:533px;display:flex}
.service{flex:1;background:#fff;border-right:1px solid #e2e2e2;height:78px}
.service h3{background:var(--brand);color:#fff;font-size:8.5px;font-weight:700;height:24px;line-height:24px;padding-left:7px;white-space:nowrap}
.service.active h3{background:#2a2a2a}
.service .body{display:flex;gap:6px;padding:9px 6px}
.service .ico{width:30px;height:30px;border-radius:50%;background:#999;flex:none}
.service.active .ico{background:#222}
.service p{font-size:6px;line-height:9px;color:var(--muted)}

/* headings */
.sec-title{font-size:15px;font-weight:700;color:#222;padding-left:10px;border-bottom:1px solid var(--rule);padding-bottom:4px;position:absolute;white-space:nowrap}
.sec-title span{color:var(--brand)}
.sec-title::before{content:"";position:absolute;left:0;top:5px;width:5px;height:5px;background:#bbb;transform:rotate(45deg)}

/* about */
.about-text{top:427px;left:81px;width:300px;font-size:6.5px;line-height:12.7px;color:var(--muted)}
.about-photo{top:406px;left:395px;width:207px;height:122px;background:linear-gradient(135deg,#9fb3c4,#d8c7b9 60%,#7e8ea0);border:3px solid #fff;box-shadow:0 2px 4px rgba(0,0,0,.3)}

/* jobs */
.jobs{top:550px;left:0;width:682px;height:240px;background:var(--band-dark)}
.jobs-photo{top:0;left:0;width:340px;height:240px;background:linear-gradient(90deg,#e8eaec,#cfd3d6 70%,#d2d2d2)}
.jobs h2{top:44px;left:335px;font-size:15px;font-weight:700;color:#333}
.job{left:335px;width:270px}
.job h4{font-size:11px;font-weight:400;display:flex;align-items:center;gap:6px;color:#333}
.job p{font-size:6.2px;line-height:11px;color:var(--muted);margin-top:4px;padding-left:2px}
.tick{width:13px;height:13px;border-radius:50%;background:#fff;display:flex;align-items:center;justify-content:center}
.apply{top:182px;left:335px;background:var(--brand);color:#fff;font-size:10px;font-weight:700;padding:6px 14px;box-shadow:2px 2px 3px rgba(0,0,0,.35)}

/* testimonial & form */
.avatar{top:845px;left:84px;width:52px;height:52px;border-radius:50%;background:linear-gradient(#c9b5a6,#7a6a60)}
.quote{top:839px;left:154px;width:177px;background:#f0f0f0;padding:7px 8px;font-size:8px;font-style:italic;line-height:13px;text-align:center;color:#444}
.quote-by{top:911px;left:179px;font-size:8px}
.divider{top:800px;left:366px;width:1px;height:160px;background:#ddd}
.field{left:389px;width:219px;height:18px;border:1px solid #ccc;background:#fff;font-size:6.5px;color:#999;display:flex;align-items:center;gap:6px;padding-left:5px}
.field.msg{height:37px;align-items:flex-start;padding-top:3px}
.submit{top:938px;left:389px;width:59px;height:16px;background:var(--brand-dark);color:#fff;font-size:8px;text-align:center;line-height:16px}

/* contacts */
.contacts{top:962px;left:0;width:682px;height:122px;background:var(--band)}
.contact-line{left:78px;font-size:7.5px;display:flex;gap:7px;color:#333;line-height:16px;white-space:nowrap}
.map{top:14px;left:389px;width:219px;height:98px;background:linear-gradient(135deg,#e9e6d6,#d8d4bf);border:1px solid #bbb}

/* footer */
.site-footer{top:1084px;left:0;width:682px;height:116px;background:var(--footer);color:#ccc}
.site-footer h5{font-size:9.5px;font-weight:400;color:#ddd;border-bottom:1px dashed #666;padding-bottom:4px}
.quick a{display:block;color:#bbb;font-size:6.5px;line-height:12.5px;text-decoration:none}
.quick a::before{content:"» ";color:#777}
.news-item{font-size:6.2px;line-height:9px;color:#bbb;padding-left:14px;position:relative;margin-top:6px}
.news-item::before{content:"";position:absolute;left:0;top:1px;width:7px;height:7px;border:1px solid #888}
.news-item em{display:block;margin-top:6px;color:#999}
.socials{display:flex;gap:3px}
.socials i{width:13px;height:13px;border-radius:50%;background:var(--brand);border:1px solid #fff;display:block}
</style>
</head>
<body>

<header class="site-header abs">
  <div class="abs brand-name" style="top:21px;left:80px"><i></i>Keelstone</div>
  <div class="abs phone">
    <svg width="12" height="12" viewBox="0 0 24 24"><path fill="#8a2a12" d="M6.6 10.8a15 15 0 006.6 6.6l2.2-2.2c.3-.3.7-.4 1-.2 1.1.4 2.3.6 3.6.6.6 0 1 .4 1 1V20c0 .6-.4 1-1 1A17 17 0 013 4c0-.6.4-1 1-1h3.5c.6 0 1 .4 1 1 0 1.3.2 2.5.6 3.6.1.3 0 .7-.2 1z"/></svg>
    Phone: 987-650-4321
  </div>
  <nav class="main-nav abs">
    <a href="#">Home</a><a href="#">About</a><a href="#">Services</a><a href="#">News</a><a href="#">Jobs</a><a href="#">Contact</a>
  </nav>
</header>

<section class="hero abs">
  <div class="hero-art abs" role="img" aria-label="Businessman holding a glowing globe network with laptop, phone and tablet"></div>
  <div class="slide-arrow abs" style="top:121px;left:48px"></div>
  <div class="slide-arrow abs" style="top:121px;left:609px"></div>
  <div class="hero-copy abs">
    <div class="kicker">WE ARE</div>
    <h1>Custom Software<br>Development</h1>
    <div class="sub">COMPANY</div>
    <p>We are a software development consulting company that writes custom software for our customers.</p>
    <span class="btn">Learn More Keelstone</span>
  </div>
</section>

<div class="services-band abs"></div>
<div class="services abs">
  <div class="service"><h3>Software Development</h3><div class="body"><span class="ico"></span><p>Lorem ipsum dolor sit, consectetuedipiscing elit, sed</p></div></div>
  <div class="service active"><h3>Strategic Outsourcing</h3><div class="body"><span class="ico"></span><p>Lorem ipsum dolor sit, consectetuedipiscing elit, sed</p></div></div>
  <div class="service"><h3>Enterprise Security</h3><div class="body"><span class="ico"></span><p>Lorem ipsum dolor sit, consectetuedipiscing elit, sed</p></div></div>
  <div class="service"><h3>Infrastructure Management</h3><div class="body"><span class="ico"></span><p>Lorem ipsum dolor sit, consectetuedipiscing elit, sed</p></div></div>
</div>

<h2 class="sec-title" style="top:396px;left:76px;width:307px">About <span>Keelstone</span></h2>
<p class="about-text abs">Lorem ipsum dolor sit amet, consectetuer adipiscing elit, sed diam nonummy nibh euismod tincidunt ut laoreet dolore magna aliquam erat volutpat. Ut wisi enim ad minim veniam, quis nostrud exerci tation ullamcorper suscipit lobortis nisl ut aliquip ex ea commodo consequat. Duis autem vel eum iriure dolor in hendrerit in vulputate velit esse molestie consequat, vel illum dolore eu feugiat nulla facilisis at vero eros et accumsan et iusto odio dignissim qui blandit praesent luptatum zzril delenit augue duis dolore te feugait nulla facilisi. Duis autem vel eum iriure dolor in hendrerit in vulputate velit esse molestie consequat, blandit praesent luptatum zzril delenit augue duis dolore te feugait nulla facilisi.</p>
<div class="about-photo abs" role="img" aria-label="Two colleagues looking at a tablet together"></div>

<section class="jobs abs">
  <div class="jobs-photo abs" role="img" aria-label="Team of three working at a laptop in a bright office"></div>
  <h2 class="abs">Current Job Opening</h2>
  <div class="job abs" style="top:73px">
    <h4><span class="tick"><svg width="8" height="8" viewBox="0 0 10 10"><path d="M1 5l3 3 5-6" stroke="#444" stroke-width="1.8" fill="none"/></svg></span>Praesent Luptatum</h4>
    <p>Lorem ipsum dolor sit amet, consectetuer adipiscing elit, sed diam nonummy euismod tincidunt ut laoreet dolore magna aliquam erat volutpat.</p>
  </div>
  <div class="job abs" style="top:125px">
    <h4><span class="tick"><svg width="8" height="8" viewBox="0 0 10 10"><path d="M1 5l3 3 5-6" stroke="#444" stroke-width="1.8" fill="none"/></svg></span>Aliquam Erat Volutpat</h4>
    <p>Duis autem vel eum iriure dolor in hendrerit in vulputate velit esse molestie consequat, vel illum dolore eu feugiat nulla facilisis</p>
  </div>
  <div class="apply abs">APPLY NOW</div>
</section>

<h2 class="sec-title" style="top:802px;left:78px;width:273px">Our <span>Clients Say</span></h2>
<div class="avatar abs" role="img" aria-label="Client portrait"></div>
<div class="quote abs">Lorem ipsum dolor sit amet, consectetuer adipiscing elit, sed diam nonummy nibh euismod tincidunt ut laoreet dolore magna aliquam erat volutpat.</div>
<div class="quote-by abs">Mr. Adrian Pellow</div>
<div class="divider abs"></div>

<h2 class="sec-title" style="top:802px;left:381px;width:227px">Get In Touch <span>With Us</span></h2>
<div class="field abs" style="top:836px">&#9679; Name</div>
<div class="field abs" style="top:857px">&#9993; Email</div>
<div class="field abs" style="top:878px">&#9742; Phone</div>
<div class="field msg abs" style="top:899px">&#9998; Massage</div>
<div class="submit abs">SUBMIT</div>

<section class="contacts abs">
  <h2 class="sec-title" style="top:16px;left:78px;width:268px">Contacts <span>Detail</span></h2>
  <div class="contact-line abs" style="top:50px"><svg width="8" height="10" viewBox="0 0 10 14"><path fill="#555" d="M5 0a5 5 0 015 5c0 4-5 9-5 9S0 9 0 5a5 5 0 015-5zm0 3a2 2 0 100 4 2 2 0 000-4z"/></svg><span>Duis autem vel eum iriure dolor in hendrerit in vulputate velit<br>esse molestie</span></div>
  <div class="contact-line abs" style="top:82px"><svg width="9" height="9" viewBox="0 0 24 24"><path fill="#555" d="M6.6 10.8a15 15 0 006.6 6.6l2.2-2.2c.3-.3.7-.4 1-.2 1.1.4 2.3.6 3.6.6.6 0 1 .4 1 1V20c0 .6-.4 1-1 1A17 17 0 013 4c0-.6.4-1 1-1h3.5c.6 0 1 .4 1 1 0 1.3.2 2.5.6 3.6.1.3 0 .7-.2 1z"/></svg><span>Call: 987-650-4321</span></div>
  <div class="contact-line abs" style="top:98px"><svg width="9" height="9" viewBox="0 0 12 9"><rect x="0.5" y="0.5" width="11" height="8" fill="none" stroke="#555"/><path d="M.5.5l5.5 4 5.5-4" fill="none" stroke="#555"/></svg><span>Email: info@keelstone-dev.com</span></div>
  <div class="map abs" role="img" aria-label="Street map showing the office location"></div>
</section>

<footer class="site-footer abs">
  <div class="abs quick" style="top:13px;left:82px;width:60px">
    <h5>Quick Link</h5>
    <div style="margin-top:3px"><a href="#">Home</a><a href="#">About</a><a href="#">Services</a><a href="#">News</a><a href="#">Jobs</a><a href="#">Contact</a></div>
  </div>
  <div class="abs" style="top:13px;left:178px;width:218px">
    <h5>Latest News</h5>
    <div class="news-item">Lorem ipsum dolor sit consectetuer adipiscing elit, sed diam nibh Lorem ipsum dolor sit consectetuer<em>20-March-2014</em></div>
    <div class="news-item">Lorem ipsum dolor sit consectetuer adipiscing elit, sed diam nibh Lorem ipsum dolor sit consectetuer adipiscing<em>20-March-2014</em></div>
  </div>
  <div class="abs" style="top:20px;left:438px;width:160px">
    <div style="display:flex;align-items:center;gap:6px;margin-top:10px">
      <span style="font-size:9.5px;color:#ddd;white-space:nowrap">Stay in Touch</span>
      <div class="socials"><i></i><i></i><i></i><i></i><i></i></div>
    </div>
    <div class="brand-name" style="color:#fff;margin:14px 0 0 24px"><i style="background:#fff"></i>Keelstone</div>
    <div style="font-size:6.3px;color:#bbb;margin-top:16px;white-space:nowrap">Copyright © 2014 Keelstone | All rights reserved.</div>
  </div>
</footer>

</body>
</html>
```